Therapy Services & Training

I provide counseling/therapy to individuals and families. I also travel the country and provide training at conferences.
I would like to see a card which takes my company name and design a logo using the letters "HWAE".
Target Market(s)
Therapists, non-profit organizations, clients looking for therapy
Industry/Entity Type
Training
Contact Information for Business Card
Harborview Wellness Advising & Education LLC
Delia Marsh, M.S.W., LCSW
Clinical Therapist & Trainer
Providing clinical therapy services to individuals, families, couples & children. We also provide life coaching and crisis training.
counselordelia@mailbrook.net
www.harborviewwellnessadvising.com
(555) 214-3092
Millbrook, IL 60999
(BACK SIDE OF CARD)
We are certified by the Ongoing Professional Lawyer Studies (OPLS) Council of the Prairie High Tribunal to provide Continuing Legal Education (CLE) credits to Illinois attorneys. Call about what courses we offer! (555) 214-3092

```html
<!DOCTYPE html>
<html lang="en">
<head>
<meta charset="utf-8">
<title>Harborview Wellness Advising &amp; Education — Business Card</title>
<link rel="stylesheet" href="https://fonts.googleapis.com/css2?family=Exo+2:wght@400;500;600;700&display=swap">
<style>
  :root {
    --bg: #e9e6e1;
    --red: #d9262c;
    --red-light: #ee3a3f;
    --red-dark: #a8161b;
    --paper: #f4f4f4;
    --paper-shade: #dcdcdc;
    --ink: #3a3a3a;
    --white: #ffffff;
    --steel-a: #5a5a5a;
    --steel-b: #c9c9c9;
    --steel-c: #8a8a8a;
  }
  * { box-sizing: border-box; margin: 0; padding: 0; }
  html, body { width: 834px; height: 1200px; overflow: hidden; }
  body {
    background: var(--bg);
    font-family: "Exo 2", sans-serif;
    color: var(--ink);
    display: flex;
    align-items: center;
    justify-content: center;
    gap: 40px;
  }
  .card {
    position: relative;
    width: 360px;
    height: 630px;
    overflow: hidden;
    box-shadow: 0 10px 30px rgba(0,0,0,.25);
  }
  .edge {
    position: absolute;
    top: 0; bottom: 0;
    width: 20px;
    background: linear-gradient(90deg, var(--steel-a), var(--steel-b) 55%, var(--steel-c));
    z-index: 2;
  }
  .edge--left { left: 0; }
  .edge--right { right: 0; }

  /* Front */
  .card--front { background: linear-gradient(180deg, var(--white), var(--paper) 50%, var(--paper-shade)); }
  .brand {
    position: absolute; top: 46px; left: 20px; right: 20px;
    text-align: center;
  }
  .brand__mark {
    display: inline-flex; align-items: center; gap: 10px;
    font-size: 50px; font-weight: 700; color: var(--red); letter-spacing: 2px;
  }
  .brand__dot { width: 16px; height: 16px; border-radius: 50%; background: var(--red); }
  .brand__name {
    margin: 8px auto 0; width: 230px;
    font-size: 14px; line-height: 1.3; color: var(--ink);
  }
  .name-band {
    position: absolute; top: 190px; left: 0; right: 0; height: 92px;
    background: linear-gradient(180deg, var(--red-light), var(--red) 60%, var(--red-dark));
    color: var(--white); text-align: center; padding-top: 14px;
  }
  .name-band__name { font-size: 32px; font-weight: 500; letter-spacing: .5px; }
  .name-band__cred { font-size: 20px; margin-top: 2px; }
  .about {
    position: absolute; top: 312px; left: 44px; right: 40px;
    font-size: 13.5px; line-height: 1.45;
  }
  .contact {
    position: absolute; top: 470px; left: 44px; right: 30px;
    list-style: none; font-size: 14px;
  }
  .contact li { display: flex; align-items: center; gap: 10px; height: 25px; }
  .contact svg { width: 14px; height: 14px; flex: none; fill: var(--red); }

  /* Back */
  .card--back { background: radial-gradient(ellipse at 50% 45%, var(--red-light), var(--red) 55%, var(--red-dark)); }
  .statement {
    position: absolute; top: 90px; left: 40px; right: 40px;
    text-align: center; color: var(--white);
    font-size: 19px; line-height: 1.55; font-weight: 500;
  }
  .cta {
    position: absolute; bottom: 46px; left: 34px; right: 34px;
    text-align: center; color: var(--white);
  }
  .cta__line { font-size: 16px; font-weight: 500; margin-bottom: 6px; }
  .cta__phone {
    display: block; background: linear-gradient(180deg, var(--white), var(--paper-shade));
    color: var(--red); font-size: 30px; font-weight: 700; letter-spacing: 2px;
    padding: 2px 0;
  }
</style>
</head>
<body>
  <article class="card card--front">
    <div class="edge edge--left"></div>
    <div class="edge edge--right"></div>
    <header class="brand">
      <div class="brand__mark"><span class="brand__dot"></span>HWAE</div>
      <p class="brand__name">Harborview Wellness Advising &amp; Education LLC</p>
    </header>
    <div class="name-band">
      <h1 class="name-band__name">Delia Marsh</h1>
      <p class="name-band__cred">M.S.W.</p>
    </div>
    <p class="about">LCSW Clinical Therapist &amp; Trainer Providing clinical therapy services to individuals, families, couples &amp; children. We also provide life coaching and crisis training.</p>
    <ul class="contact">
      <li><svg viewBox="0 0 16 16"><path d="M8 0a5.5 5.5 0 0 0-5.5 5.5C2.5 10 8 16 8 16s5.5-6 5.5-10.5A5.5 5.5 0 0 0 8 0zm0 8a2.5 2.5 0 1 1 0-5 2.5 2.5 0 0 1 0 5z"/></svg>Millbrook, IL 60999</li>
      <li><svg viewBox="0 0 16 16"><path d="M3.6 1 6 3.8 4.7 5.6a10 10 0 0 0 5.7 5.7L12.2 10 15 12.4 13.5 15C6.8 14.7 1.3 9.2 1 2.5z"/></svg>(555) 214-3092</li>
      <li><svg viewBox="0 0 16 16"><path d="M0 3h16v1.2L8 9 0 4.2z"/><path d="M0 5.6 8 10.4l8-4.8V13H0z"/></svg>counselordelia@mailbrook.net</li>
      <li><svg viewBox="0 0 16 16"><path d="M8 0a8 8 0 1 0 0 16A8 8 0 0 0 8 0zm5.9 7.2h-2.6a12 12 0 0 0-1-4.9 6.4 6.4 0 0 1 3.6 4.9zM8 1.7c.8 1 1.6 2.9 1.7 5.5H6.3C6.4 4.6 7.2 2.7 8 1.7zM5.7 2.3a12 12 0 0 0-1 4.9H2.1a6.4 6.4 0 0 1 3.6-4.9zM2.1 8.8h2.6a12 12 0 0 0 1 4.9 6.4 6.4 0 0 1-3.6-4.9zM8 14.3c-.8-1-1.6-2.9-1.7-5.5h3.4c-.1 2.6-.9 4.5-1.7 5.5zm2.3-.6a12 12 0 0 0 1-4.9h2.6a6.4 6.4 0 0 1-3.6 4.9z"/></svg>www.harborviewwellnessadvising.com</li>
    </ul>
  </article>

  <article class="card card--back">
    <div class="edge edge--left"></div>
    <div class="edge edge--right"></div>
    <p class="statement">We are certified by the Ongoing Professional Lawyer Studies (OPLS) Council of the Prairie High Tribunal to provide Continuing Legal Education (CLE) credits to Illinois attorneys.</p>
    <div class="cta">
      <p class="cta__line">Call about what courses we offer!</p>
      <span class="cta__phone">(555) 214-3092</span>
    </div>
  </article>
</body>
</html>
```